Electrical contractor in San Diego county since 1988

Provide a company name/ logo for business cards and forms. Newer and more modern old card is attached. Color preference is black and orange. Simple and streamlined nothing too busy. I have also attached a card that represents the simplicity of what we are looking for.

Contractor

```html
<!DOCTYPE html>
<html lang="en">
<head>
<meta charset="utf-8">
<title>Veltra Coast Construction – Business Card</title>
<link href="https://fonts.googleapis.com/css2?family=Arimo:wght@400;700&display=swap" rel="stylesheet">
<style>
  :root {
    --page: #e9e4dc;
    --card: #1d1b1c;
    --orange: #f47b20;
    --orange-text: #f08a2c;
    --edge-shadow: #6b6461;
    --mark: #3f9a3c;
  }
  * { margin: 0; padding: 0; box-sizing: border-box; }
  html, body {
    width: 1200px;
    height: 832px;
    overflow: hidden;
    background: var(--page);
    font-family: "Arimo", Arial, sans-serif;
  }
  .business-card {
    position: absolute;
    left: 100px;
    top: 111px;
    width: 1000px;
    height: 610px;
    background: var(--card);
    box-shadow: 0 10px 30px rgba(0,0,0,0.25);
    overflow: hidden;
  }
  .card-edges {
    position: absolute;
    inset: 0;
    width: 100%;
    height: 100%;
  }
  .company-lockup {
    position: absolute;
    left: 192px;
    top: 240px;
    display: flex;
    align-items: center;
    gap: 22px;
  }
  .company-square {
    width: 86px;
    height: 86px;
    background: var(--mark);
  }
  .company-name {
    color: var(--orange-text);
    font-weight: 700;
    font-size: 40px;
    line-height: 1.1;
    letter-spacing: 2px;
    text-transform: uppercase;
  }
  .company-name span { display: block; }
  .holder {
    position: absolute;
    left: 303px;
    top: 362px;
    color: var(--orange-text);
    font-size: 30px;
  }
  .contact {
    position: absolute;
    top: 462px;
    color: var(--orange-text);
    font-size: 29px;
    line-height: 36px;
  }
  .contact--mail { left: 97px; }
  .contact--phone { right: 104px; text-align: right; }
</style>
</head>
<body>
  <main class="business-card">
    <svg class="card-edges" viewBox="0 0 1000 610" preserveAspectRatio="none" aria-hidden="true">
      <path d="M0 0 H1000 V34 Q500 -6 0 34 Z" fill="var(--orange)"/>
      <path d="M0 34 Q500 -6 1000 34" fill="none" stroke="var(--edge-shadow)" stroke-width="4"/>
      <path d="M0 610 H1000 V572 Q500 612 0 572 Z" fill="var(--orange)"/>
      <path d="M0 572 Q500 612 1000 572" fill="none" stroke="var(--edge-shadow)" stroke-width="4"/>
    </svg>

    <div class="company-lockup">
      <div class="company-square"></div>
      <div class="company-name">
        <span>Veltra Coast</span>
        <span>Construction</span>
      </div>
    </div>

    <p class="holder">DANIEL MARSH - President</p>

    <address class="contact contact--mail" style="font-style: normal;">
      P.O.Box 4827<br>
      Harbor Vale, CA 91234-567
    </address>

    <p class="contact contact--phone">
      (555) 210-4836<br>
      Fax 210-7752
    </p>
  </main>
</body>
</html>
```